Web Calculator design Housing Investment

We have a web calculator that needs to be fixed from a design perspective. The key tasks are:<br/>1. Selecting icons / pictures / colours for the various steps<br/>2. Designing navigation between calculator steps<br/>3. Making suggestions for chart design. The limitation is that the charts are all using the Plovik API (the same charts that Plovik Grids use).<br/><br/>There are four entry screens and then a result screen. See attached PDF for screenshots. You can see our website at https://ambertidefunds.com for our corporate colours and style.

Target Market(s)

Real Estate Investors

Industry/Entity Type

Financial Planning

Number of Pages Required

1 page

Font styles to use
Sans Serif
Other font styles liked:
• Ubuntu

Colors
86cae7
3176b5
0455a3
ffffff

Requirements
Must have
• New Icons
• Suggested design for navigation
• Suggested design for charts

```html
<!DOCTYPE html>
<html lang="en">
<head>
<meta charset="utf-8">
<title>Property Calculator – Ambertide Funds</title>
<link href="https://fonts.googleapis.com/css2?family=Ubuntu:wght@400;500;700&display=swap" rel="stylesheet">
<style>
:root{
  --page:#eff1f5;
  --white:#ffffff;
  --brand:#0659a5;
  --brand-dark:#0455a3;
  --mid:#3176b5;
  --sky:#86cae7;
  --pale:#c7d9ec;
  --ink:#1d1d1f;
  --muted:#4a4a4a;
  --line:#cfd3d9;
  --footer:#000000;
  --panel:#23272d;
  --panel-edge:#3a3f46;
}
*{box-sizing:border-box;margin:0;padding:0}
html,body{width:1200px;height:2607px;overflow:hidden}
body{background:var(--page);font-family:"Ubuntu",sans-serif;color:var(--ink);position:relative}
.screen{position:relative;width:1200px}
.site-footer{height:45px;background:var(--footer);color:var(--white);font-size:12px;display:flex;align-items:center;justify-content:center}
.site-footer.tall{height:46px}

/* stepper */
.stepper{position:absolute;left:94px;top:24px;width:1012px;height:36px;background:var(--white);box-shadow:0 2px 4px rgba(0,0,0,.08);overflow:hidden}
.step{position:absolute;top:7px;display:flex;align-items:center;font-size:11.5px;color:var(--ink);white-space:nowrap}
.step-num{width:22px;height:22px;border-radius:50%;border:1px solid var(--line);background:var(--white);color:#777;font-size:11px;display:flex;align-items:center;justify-content:center;margin-right:6px}
.step.active .step-num{background:var(--brand);border-color:var(--brand);color:var(--white);font-weight:700}
.step-link{position:absolute;top:17px;height:1px;background:var(--line)}
.nav-btn{position:absolute;top:6px;height:24px;font-size:11.5px;font-weight:700;display:flex;align-items:center;justify-content:center;font-family:inherit;border:0;white-space:nowrap;padding:0}
.nav-btn.primary{background:var(--brand);color:var(--white)}
.nav-btn.secondary{background:var(--pale);color:var(--ink)}
.btn-next{width:45px}
.btn-prev{width:61px}
.btn-recalc{width:72px}

.screen-title{position:absolute;left:0;width:1200px;text-align:center;font-size:16.5px;font-weight:500}

/* screen 1 */
.type-card{position:absolute;top:156px;width:238px;height:286px;background:var(--white);box-shadow:0 2px 6px rgba(0,0,0,.1)}
.type-art{position:absolute;left:0;top:0;width:238px;height:249px}
.type-label{position:absolute;left:0;bottom:0;width:238px;height:37px;background:var(--brand);color:var(--white);font-size:17px;font-weight:500;display:flex;align-items:center;justify-content:center}

/* screen 2 */
.location-panel{position:absolute;left:297px;top:140px;width:606px;height:286px;background:var(--brand)}
.map-disc{position:absolute;left:39px;top:49px;width:188px;height:188px;border-radius:50%;background:var(--white);border:4px solid var(--sky);overflow:hidden}
.slider-label{position:absolute;color:var(--white);font-size:11.5px}
.slider-track{position:absolute;height:1px;background:var(--pale)}
.slider-knob{position:absolute;width:12px;height:12px;border-radius:50%;border:2px solid var(--white);background:var(--brand)}
.slider-value{position:absolute;color:var(--white);font-size:11.5px}

/* screen 3 */
.method-card{position:absolute;top:201px;width:261px;height:170px;background:var(--white);border-radius:0 32px 32px 0;box-shadow:0 3px 8px rgba(0,0,0,.1);text-align:center}
.method-icon{position:absolute;top:-53px;left:79px;width:114px;height:114px;border-radius:50%;background:var(--white);border:3px solid var(--brand);overflow:hidden}
.method-icon span{display:block;width:100%;height:100%}
.method-name{position:absolute;top:74px;width:100%;font-size:15px;font-weight:700}
.method-text{position:absolute;top:114px;left:30px;right:30px;font-size:11.5px;line-height:17px;color:var(--muted)}

/* screen 4 */
.forecast-row{position:absolute;left:370px;font-size:11.5px;line-height:16px;color:var(--ink);width:300px}
.select-box{position:absolute;left:686px;width:139px;height:30px;background:var(--brand);color:var(--white);font-size:11px;font-weight:700;display:flex;align-items:center;padding-left:10px}
.select-box svg{position:absolute;right:8px;top:11px}
.chart-frame{position:absolute;left:317px;top:259px;width:566px;height:282px;background:var(--brand)}
.chart-sheet{position:absolute;left:15px;top:15px;width:536px;height:250px;background:var(--white)}

/* screen 5 */
.result-panel{position:absolute;left:94px;top:107px;width:1012px;height:274px;background:var(--brand)}
.result-sheet{position:absolute;left:15px;top:15px;width:982px;height:156px;background:var(--white)}
.result-dark{position:absolute;left:21px;top:17px;width:940px;height:122px;background:#1b1e22}
.result-box{position:absolute;top:7px;height:108px;background:var(--panel);border:1px solid var(--panel-edge)}
.result-note{position:absolute;left:0;top:192px;width:1012px;text-align:center;color:var(--white);font-size:11.5px;line-height:17px}
.result-rule{position:absolute;left:138px;top:237px;width:736px;height:1px;background:var(--pale)}
.tiny{font-size:6px;fill:#c9ccd1;font-family:"Ubuntu",sans-serif}
</style>
</head>
<body>

<!-- Step 1 -->
<section class="screen" style="height:486px">
  <div class="stepper">
    <div class="step active" style="left:6px"><span class="step-num">1</span>Property Type</div>
    <div class="step-link" style="left:112px;width:60px"></div>
    <div class="step" style="left:172px"><span class="step-num">2</span>Property Location</div>
    <div class="step-link" style="left:300px;width:65px"></div>
    <div class="step" style="left:365px"><span class="step-num">3</span>Property Valuation</div>
    <div class="step-link" style="left:497px;width:71px"></div>
    <div class="step" style="left:568px"><span class="step-num">4</span>Your Property Forecast</div>
    <div class="step-link" style="left:720px;width:58px"></div>
    <div class="step" style="left:778px"><span class="step-num">5</span>Calculation</div>
    <button class="nav-btn primary btn-next" style="left:961px">Next</button>
  </div>
  <h2 class="screen-title" style="top:103px">What Type Of Property would You Like To Compare?</h2>
  <div class="type-card" style="left:354px">
    <div class="type-art" role="img" aria-label="Illustration of blue apartment towers" style="background:radial-gradient(ellipse at 50% 55%,#3f86d4 0%,#a9cdf0 45%,#f3f8fd 75%)"></div>
    <div class="type-label">Unit</div>
  </div>
  <div class="type-card" style="left:609px">
    <div class="type-art" role="img" aria-label="Illustration of a light blue family house on a lawn" style="background:radial-gradient(ellipse at 50% 52%,#7cc7ee 0%,#c3e6f6 35%,#ffffff 62%)"></div>
    <div class="type-label">House</div>
  </div>
</section>
<footer class="site-footer">Copyright 2019 © Ambertide Funds. All Right Reserved.</footer>

<!-- Step 2 -->
<section class="screen" style="height:469px">
  <div class="stepper">
    <div class="step" style="left:6px"><span class="step-num">1</span>Property Type</div>
    <div class="step-link" style="left:112px;width:60px"></div>
    <div class="step active" style="left:172px"><span class="step-num">2</span>Property Location</div>
    <div class="step-link" style="left:300px;width:65px"></div>
    <div class="step" style="left:365px"><span class="step-num">3</span>Property Valuation</div>
    <div class="step-link" style="left:497px;width:71px"></div>
    <div class="step" style="left:568px"><span class="step-num">4</span>Your Property Forecast</div>
    <div class="step-link" style="left:720px;width:58px"></div>
    <div class="step" style="left:778px"><span class="step-num">5</span>Calculation</div>
    <button class="nav-btn secondary btn-prev" style="left:897px">Previous</button>
    <button class="nav-btn primary btn-next" style="left:961px">Next</button>
  </div>
  <h2 class="screen-title" style="top:103px">Where Would This Property Be Located?</h2>
  <div class="location-panel">
    <div class="map-disc"><div role="img" aria-label="Map of Australia with states in shades of blue" style="width:100%;height:100%;background:radial-gradient(ellipse at 50% 48%,#4aa6f0 0%,#7cc2f5 40%,#f7f9fb 70%)"></div></div>
    <div class="slider-label" style="left:253px;top:88px">How Much Will The Property Cost:
      <svg width="11" height="11" viewBox="0 0 11 11" style="vertical-align:-1px;margin-left:3px"><circle cx="5.5" cy="5.5" r="4.7" fill="none" stroke="#fff"/><path d="M5.5 4.7v3.4M5.5 3v.2" stroke="#fff" stroke-linecap="round"/></svg></div>
    <div class="slider-track" style="left:230px;top:119px;width:275px"></div>
    <div class="slider-knob" style="left:302px;top:113px"></div>
    <div class="slider-value" style="left:518px;top:112px">$500,000</div>
    <div class="slider-label" style="left:258px;top:156px">How Much Will You Invest?
      <svg width="11" height="11" viewBox="0 0 11 11" style="vertical-align:-1px;margin-left:3px"><circle cx="5.5" cy="5.5" r="4.7" fill="none" stroke="#fff"/><path d="M5.5 4.7v3.4M5.5 3v.2" stroke="#fff" stroke-linecap="round"/></svg></div>
    <div class="slider-track" style="left:242px;top:187px;width:263px"></div>
    <div class="slider-knob" style="left:276px;top:181px"></div>
    <div class="slider-value" style="left:518px;top:180px">$200,000</div>
  </div>
</section>
<footer class="site-footer">Copyright 2019 © Ambertide Funds. All Right Reserved.</footer>

<!-- Step 3 -->
<section class="screen" style="height:415px">
  <div class="stepper">
    <div class="step" style="left:6px"><span class="step-num">1</span>Property Type</div>
    <div class="step-link" style="left:112px;width:60px"></div>
    <div class="step" style="left:172px"><span class="step-num">2</span>Property Location</div>
    <div class="step-link" style="left:300px;width:65px"></div>
    <div class="step active" style="left:365px"><span class="step-num">3</span>Property Valuation</div>
    <div class="step-link" style="left:497px;width:71px"></div>
    <div class="step" style="left:568px"><span class="step-num">4</span>Your Property Forecast</div>
    <div class="step-link" style="left:720px;width:58px"></div>
    <div class="step" style="left:778px"><span class="step-num">5</span>Calculation</div>
    <button class="nav-btn secondary btn-prev" style="left:897px">Previous</button>
    <button class="nav-btn primary btn-next" style="left:961px">Next</button>
  </div>
  <h2 class="screen-title" style="top:104px">How Would You Like To Forecast The Returns Form Property?</h2>
  <div class="method-card" style="left:188px">
    <div class="method-icon"><span role="img" aria-label="Illustration of a calculator with banknotes and coins" style="background:radial-gradient(circle,#d8b04a 0%,#8fae6a 40%,#ffffff 70%)"></span></div>
    <div class="method-name">Relative Cost</div>
    <div class="method-text">Use this to value property based on mortgage relative to rent cost</div>
  </div>
  <div class="method-card" style="left:472px">
    <div class="method-icon"><span role="img" aria-label="Illustration of a balance scale weighing money against a clock" style="background:radial-gradient(circle,#e0a24a 0%,#b88c6a 40%,#ffffff 70%)"></span></div>
    <div class="method-name">Relative To Wages</div>
    <div class="method-text">Use this to value property based on mortgage relative to wages</div>
  </div>
  <div class="method-card" style="left:755px">
    <div class="method-icon"><span role="img" aria-label="Illustration of a large percent sign with coins and a figure" style="background:radial-gradient(circle,#f2cf6a 0%,#f5e2a8 40%,#ffffff 70%)"></span></div>
    <div class="method-name">Using Rental Yield</div>
    <div class="method-text">Use this to value property based on<br>a rental yield</div>
  </div>
</section>
<footer class="site-footer tall">Copyright 2019 © Ambertide Funds. All Right Reserved.</footer>

<!-- Step 4 -->
<section class="screen" style="height:585px">
  <div class="stepper">
    <div class="step" style="left:6px"><span class="step-num">1</span>Property Type</div>
    <div class="step-link" style="left:112px;width:60px"></div>
    <div class="step" style="left:172px"><span class="step-num">2</span>Property Location</div>
    <div class="step-link" style="left:300px;width:65px"></div>
    <div class="step" style="left:365px"><span class="step-num">3</span>Property Valuation</div>
    <div class="step-link" style="left:497px;width:71px"></div>
    <div class="step active" style="left:568px"><span class="step-num">4</span>Your Property Forecast</div>
    <div class="step-link" style="left:720px;width:58px"></div>
    <div class="step" style="left:778px"><span class="step-num">5</span>Calculation</div>
    <button class="nav-btn secondary btn-prev" style="left:897px">Previous</button>
    <button class="nav-btn primary btn-next" style="left:961px">Next</button>
  </div>
  <h2 class="screen-title" style="top:104px">Your Property Price Forecast</h2>
  <p class="forecast-row" style="top:151px">You have chosen to forecast property priceing</p>
  <div class="select-box" style="top:145px">Gross Tental Yield<svg width="9" height="6" viewBox="0 0 9 6"><path d="M1 1l3.5 3.5L8 1" fill="none" stroke="#fff" stroke-width="1.6"/></svg></div>
  <p class="forecast-row" style="top:197px">You can see how this ratio has charged over time (in blue) below vs your assumption (in red) for</p>
  <div class="select-box" style="top:199px">Sydney House<svg width="9" height="6" viewBox="0 0 9 6"><path d="M1 1l3.5 3.5L8 1" fill="none" stroke="#fff" stroke-width="1.6"/></svg></div>
  <div class="chart-frame">
    <div class="chart-sheet">
      <svg width="536" height="250" viewBox="0 0 536 250">
        <rect x="66" y="6" width="404" height="182" fill="#f7f8f9"/>
        <rect x="88" y="12" width="354" height="108" fill="#fff" stroke="#e4e6e9"/>
        <line x1="222" y1="22" x2="234" y2="22" stroke="#4a9de0"/><text x="237" y="24" class="tiny" style="fill:#777;font-size:5.5px">Gross Rental Yield</text>
        <line x1="295" y1="22" x2="307" y2="22" stroke="#3450c8"/><text x="310" y="24" class="tiny" style="fill:#777;font-size:5.5px">Forecast</text>
        <g stroke="#eceef0"><line x1="115" y1="32" x2="435" y2="32"/><line x1="115" y1="56" x2="435" y2="56"/><line x1="115" y1="80" x2="435" y2="80"/><line x1="115" y1="104" x2="435" y2="104"/></g>
        <g class="tiny" style="fill:#888;font-size:5.5px"><text x="100" y="34">15%</text><text x="100" y="58">10%</text><text x="103" y="82">5%</text><text x="103" y="106">0%</text>
        <text x="140" y="114">1985</text><text x="173" y="114">1990</text><text x="205" y="114">1995</text><text x="238" y="114">2000</text><text x="270" y="114">2005</text><text x="303" y="114">2010</text><text x="335" y="114">2015</text><text x="367" y="114">2020</text><text x="400" y="114">2025</text></g>
        <polyline fill="none" stroke="#4a9de0" stroke-width="1" points="117,57 121,64 125,60 130,66 136,58 142,62 148,57 154,55 158,60 164,56 170,63 178,62 186,66 194,64 202,67 212,65 222,68 232,66 240,70 248,74 256,78 266,82 276,80 286,83 296,79 306,82 316,81 326,84 336,82 346,85 352,88 360,86 366,88"/>
        <line x1="366" y1="88" x2="434" y2="88" stroke="#3450c8" stroke-width="1"/>
        <text x="86" y="142" class="tiny" style="fill:#888;font-size:5.8px">By default we assume the ratio stays at the latest value of 3.4%. You can change this assumption using the slider.</text>
        <line x1="84" y1="160" x2="138" y2="160" stroke="#86cae7" stroke-width="2"/>
        <line x1="138" y1="160" x2="442" y2="160" stroke="#e1e4e8" stroke-width="1"/>
        <circle cx="138" cy="160" r="3" fill="#fff" stroke="#4a9de0"/>
        <text x="262" y="174" class="tiny" style="fill:#888;font-size:5.8px">3.4%</text>
      </svg>
    </div>
  </div>
</section>
<footer class="site-footer tall">Copyright 2019 © Ambertide Funds. All Right Reserved.</footer>

<!-- Step 5 -->
<section class="screen" style="height:425px">
  <div class="stepper">
    <div class="step" style="left:6px"><span class="step-num">1</span>Property Type</div>
    <div class="step-link" style="left:112px;width:60px"></div>
    <div class="step" style="left:172px"><span class="step-num">2</span>Property Location</div>
    <div class="step-link" style="left:300px;width:65px"></div>
    <div class="step" style="left:365px"><span class="step-num">3</span>Property Valuation</div>
    <div class="step-link" style="left:497px;width:71px"></div>
    <div class="step" style="left:568px"><span class="step-num">4</span>Your Property Forecast</div>
    <div class="step-link" style="left:720px;width:58px"></div>
    <div class="step active" style="left:778px"><span class="step-num">5</span>Calculation</div>
    <button class="nav-btn primary btn-prev" style="left:874px">Previous</button>
    <button class="nav-btn secondary btn-recalc" style="left:937px">Recaluclate</button>
  </div>
  <div class="result-panel">
    <div class="result-sheet">
      <div class="result-dark">
        <div class="result-box" style="left:4px;width:298px;background:transparent;border:0">
          <svg width="298" height="108" viewBox="0 0 298 108">
            <g class="tiny"><text x="84" y="10">Choose Property:</text><text x="45" y="35">Choose Alternative Investment:</text><text x="28" y="61">How much will the property cost? ⓘ:</text><text x="48" y="88">How much will you invest? ⓘ:</text></g>
            <rect x="137" y="3" width="127" height="11" fill="#2d3238" stroke="#555"/><text x="142" y="11" class="tiny">Sydney House</text><path d="M254 7l2 2 2-2" stroke="#ccc" fill="none"/>
            <rect x="137" y="28" width="127" height="11" fill="#2d3238" stroke="#555"/><text x="142" y="36" class="tiny">Global Shares</text><path d="M254 32l2 2 2-2" stroke="#ccc" fill="none"/>
            <line x1="140" y1="59" x2="170" y2="59" stroke="#6fb6ea" stroke-width="1.5"/><circle cx="170" cy="59" r="2.5" fill="#23272d" stroke="#6fb6ea"/><text x="272" y="62" class="tiny">$500,000</text>
            <line x1="140" y1="86" x2="152" y2="86" stroke="#6fb6ea" stroke-width="1.5"/><circle cx="152" cy="86" r="2.5" fill="#23272d" stroke="#6fb6ea"/><text x="272" y="89" class="tiny">$200,000</text>
          </svg>
        </div>
        <div class="result-box" style="left:313px;width:224px">
          <svg width="224" height="108" viewBox="0 0 224 108">
            <g class="tiny" style="font-size:5px"><text x="10" y="20">200K</text><text x="10" y="44">100K</text><text x="16" y="68">0</text><text x="8" y="92">-100K</text>
            <text x="26" y="103">2019</text><text x="61" y="103">2021</text><text x="96" y="103">2023</text><text x="131" y="103">2025</text><text x="166" y="103">2027</text><text x="200" y="103">2029</text></g>
            <line x1="32" y1="66" x2="212" y2="66" stroke="#555"/>
            <polyline points="32,72 80,64 130,56 180,48 210,42" fill="none" stroke="#4a9de0"/>
            <polyline points="32,70 80,68 130,66 180,64 210,62" fill="none" stroke="#3a6fd0"/>
            <polyline points="32,70 70,76 120,73 170,70 210,68" fill="none" stroke="#2fa6b5"/>
            <text x="60" y="52" class="tiny" style="font-size:5px;fill:#4a9de0">Shares</text><text x="150" y="52" class="tiny" style="font-size:5px;fill:#4a9de0">Property if no debt</text><text x="95" y="72" class="tiny" style="font-size:5px;fill:#3a6fd0">Property</text>
          </svg>
        </div>
        <div class="result-box" style="left:548px;width:224px">
          <svg width="224" height="108" viewBox="0 0 224 108">
            <rect x="64" y="6" width="10" height="4" fill="#2f8fe6"/><text x="76" y="10" class="tiny" style="font-size:5px">Shares Cashflow</text>
            <rect x="122" y="6" width="10" height="4" fill="#4456d8"/><text x="134" y="10" class="tiny" style="font-size:5px">Property Cashflow</text>
            <g class="tiny" style="font-size:5px"><text x="10" y="24">10K</text><text x="16" y="46">0</text><text x="8" y="68">-10K</text><text x="8" y="90">-20K</text>
            <text x="26" y="103">2019</text><text x="61" y="103">2021</text><text x="96" y="103">2023</text><text x="131" y="103">2025</text><text x="166" y="103">2027</text><text x="200" y="103">2029</text></g>
            <line x1="32" y1="44" x2="212" y2="44" stroke="#555"/>
            <g fill="#2f8fe6"><rect x="40" y="40" width="6" height="4"/><rect x="57" y="40" width="6" height="4"/><rect x="74" y="40" width="6" height="4"/><rect x="91" y="40" width="6" height="4"/><rect x="108" y="40" width="6" height="4"/><rect x="125" y="39" width="6" height="5"/><rect x="142" y="39" width="6" height="5"/><rect x="159" y="39" width="6" height="5"/><rect x="176" y="39" width="6" height="5"/><rect x="193" y="38" width="6" height="6"/></g>
            <g fill="#4456d8"><rect x="47" y="44" width="6" height="10"/><rect x="64" y="44" width="6" height="12"/><rect x="81" y="44" width="6" height="13"/><rect x="98" y="44" width="6" height="14"/><rect x="115" y="44" width="6" height="15"/><rect x="132" y="44" width="6" height="16"/><rect x="149" y="44" width="6" height="17"/><rect x="166" y="44" width="6" height="18"/><rect x="183" y="44" width="6" height="19"/><rect x="200" y="44" width="6" height="20"/></g>
          </svg>
        </div>
        <div class="result-box" style="left:783px;width:152px">
          <svg width="152" height="108" viewBox="0 0 152 108">
            <g font-family="Ubuntu, sans-serif" fill="#fff" text-anchor="middle">
              <text x="76" y="19" font-size="9">After 5 years:</text>
              <text x="76" y="34" font-size="6.5">Shares will return $82,431 more ⓘ</text>
              <text x="76" y="61" font-size="9">After 10 years:</text>
              <text x="76" y="76" font-size="6.5">Shares will return $160,176 more ⓘ</text>
              <text x="76" y="91" font-size="9">Debt Contribution ⓘ</text>
            </g>
          </svg>
        </div>
      </div>
    </div>
    <p class="result-note"><b>Note:</b> These are indicative figures based on a boad range of assumtion (below). Plese cotact Ambertide Funds or a financial planner before<br>makin any investment based on the assumtions from this calculato</p>
    <div class="result-rule"></div>
  </div>
</section>
<footer class="site-footer">Copyright 2019 © Ambertide Funds. All Right Reserved.</footer>

</body>
</html>
```